Lorvika.no is a new website about pedagogical entrepreneurship. It's main target group is teachers. The Fjellmark Institute for Classroom Media and the Nordvik Agency for Schools and Study are leading the project.

The web page is meant to show examples of how different methods of entrepreneurship can be used pedagogical in a learning environment. The page will also support the user with examples of different teaching programs and other examples of best practice.

Pedagogical entrepreneurship is not about business and men in suits. It's a method for learning. The focus in the design should be on school, education and new ways of learning.

The final product should be motivating and engaging, but at the same time governmental and serious. We are not looking for something "flashy" and corporate-looking, but a moderate, task-focused and clean design that state quality.

We need designs for three pages:
1 - frontpage
2 - subpage ("Metoder og undervisningsopplegg")
3 - subpage ("Smått-VERK i Brekkelia")

The interaction design for these three pages will be uploaded as an attachment.

We would like you to find inspiration in the following websites:
- www.gryvekst.no
- www.lavrek.no
- www.tovandstudio.com
- www.kvp.no
(more will be added)

Please use the attached logo, and feel free to use this as an inspiration for the rest of the design.

Target Market(s)

Teachers

Industry/Entity Type

Education

Requirements
Must have
• * Header with: Logo. Main navigation. Utility navigation. Search box.
* Footer
Should not have
• Images of men in suits.
Very strong graphical elements that stands out too much (we want it clean).

```html
<!DOCTYPE html>
<html lang="en">
<head>
<meta charset="utf-8">
<title>Lorvika.no – Smått-VERK i Brekkelia</title>
<link rel="stylesheet" href="https://fonts.googleapis.com/css2?family=Open+Sans:wght@400;600;700&family=Arimo:wght@400;700&display=swap">
<style>
  :root {
    --stage-top: #cdd2d6;
    --stage-mid: #5b7f94;
    --stage-deep: #0e4a6b;
    --footer-top: #6f8fa3;
    --panel-light: #ffffff;
    --panel-fade: #e3e4e5;
    --brand-blue: #2a8fd0;
    --title-blue: #1d4f7a;
    --nav-grey: #cbcbcb;
    --nav-active: #1b5878;
    --text: #222222;
    --muted: #777777;
    --link-light: #9fd3f5;
    --thumb-link: #b9c8d2;
    --tab-grey: #5a5a5a;
  }
  * { box-sizing: border-box; margin: 0; padding: 0; }
  html, body { width: 940px; height: 1200px; overflow: hidden; background: #ffffff; }
  body { font-family: "Arimo", Arial, sans-serif; color: var(--text); }
  .canvas { position: relative; width: 940px; height: 1200px; overflow: hidden; }

  .stage {
    position: absolute; left: 37px; top: 38px; width: 864px; height: 1109px;
    background: linear-gradient(180deg, var(--stage-top) 0%, #9fb0bb 22%, var(--stage-mid) 40%, #2a6283 62%, var(--stage-deep) 100%);
  }

  /* Header */
  .brand { position: absolute; left: 90px; top: 60px; display: flex; align-items: center; gap: 10px; }
  .brand-mark { width: 42px; height: 42px; border-radius: 50%; background: #ffffff; }
  .brand-name { font-family: "Open Sans", sans-serif; font-weight: 700; font-size: 40px; color: var(--brand-blue); line-height: 1; }
  .brand-tagline { position: absolute; left: 166px; top: 104px; font-family: "Open Sans", sans-serif; font-size: 8px; color: #ffffff; font-weight: 600; }
  .breadcrumb { position: absolute; right: 79px; top: 132px; font-size: 7px; color: #5d6870; font-weight: 700; }
  .breadcrumb .current { color: var(--title-blue); text-decoration: underline; }

  /* Side panel */
  .side-panel {
    position: absolute; left: 91px; top: 176px; width: 260px; height: 644px; border-radius: 14px;
    background: linear-gradient(180deg, var(--panel-light) 0%, var(--panel-fade) 100%);
    box-shadow: 0 4px 14px rgba(0,0,0,.25);
  }
  .main-nav { position: absolute; left: 15px; top: 18px; width: 212px; list-style: none; }
  .main-nav li {
    height: 41px; margin-bottom: 7px; padding: 8px 0 0 47px; background: var(--nav-grey);
    font-family: "Open Sans", sans-serif; font-size: 9.5px; line-height: 13px; color: #ffffff; text-transform: uppercase;
    box-shadow: 0 2px 3px rgba(0,0,0,.2);
  }
  .main-nav li.active { background: linear-gradient(180deg, #246584, var(--nav-active)); }
  .multimedia { position: absolute; left: 22px; top: 274px; }
  .multimedia h3 { font-size: 13px; color: #555555; font-weight: 700; margin-bottom: 4px; }
  .media-tabs { display: flex; gap: 8px; margin-bottom: 5px; }
  .media-tabs span { background: var(--tab-grey); color: #ffffff; font-size: 10px; padding: 1px 7px; }
  .video-frame {
    position: relative; width: 191px; height: 122px; border: 3px solid #8a8a8a;
    background: linear-gradient(180deg, #1c5576 0%, #7a9bb0 55%, #eceef0 100%);
  }
  .video-frame svg { position: absolute; left: 10px; bottom: 6px; }

  /* Main panel */
  .main-panel {
    position: absolute; left: 318px; top: 147px; width: 557px; height: 834px; border-radius: 14px; overflow: hidden;
    background: linear-gradient(180deg, var(--panel-light) 0%, var(--panel-fade) 80%);
    box-shadow: 0 6px 20px rgba(0,0,0,.3);
  }
  .utility-nav { position: absolute; left: 39px; top: 17px; display: flex; gap: 26px; font-size: 10px; }
  .utility-nav a { color: var(--muted); text-decoration: underline; }
  .search { position: absolute; left: 393px; top: 16px; display: flex; }
  .search input { width: 117px; height: 16px; border: 1px solid #d4d4d4; font-size: 9px; padding: 0 5px; color: #777; font-family: inherit; }
  .search button { width: 17px; height: 16px; border: none; background: #c8c8c8; display: flex; align-items: center; justify-content: center; }

  .article-head { position: absolute; left: 39px; top: 58px; width: 295px; }
  .article-head h1 { font-size: 13.5px; color: var(--title-blue); margin-bottom: 13px; }
  .lead { font-size: 10.5px; font-weight: 700; line-height: 15px; margin-bottom: 13px; }
  .intro { font-size: 10px; line-height: 14.5px; }
  .facts { position: absolute; left: 42px; top: 218px; display: flex; gap: 22px; }
  .fact { font-size: 6.5px; color: #777; line-height: 8px; width: 58px; }
  .fact svg { display: block; margin-bottom: 4px; }

  .school-card { position: absolute; left: 392px; top: 70px; width: 134px; }
  .school-id { display: flex; gap: 4px; align-items: flex-start; margin-bottom: 5px; }
  .school-id .badge { width: 33px; height: 22px; border-radius: 3px; background: #c9c9c9; }
  .school-id b { display: block; font-size: 8.5px; color: #555; }
  .school-id small { font-size: 7px; color: #444; }
  .school-photo { width: 134px; height: 111px; background: linear-gradient(180deg, #c9d3da 0%, #3f6d88 100%); }
  .contact { display: flex; gap: 6px; margin-top: 7px; }
  .contact b { display: block; font-size: 10px; color: #555; }
  .contact small { font-size: 7px; color: #444; }

  .article-body { position: absolute; left: 39px; top: 303px; width: 487px; }
  .article-body h2 { font-size: 12.5px; font-weight: 700; margin-bottom: 6px; }
  .article-body h3 { font-size: 12.5px; font-weight: 700; margin-bottom: 2px; }
  .article-body p { font-size: 11.3px; line-height: 17.2px; margin-bottom: 9px; }

  .related { position: absolute; left: 0; top: 672px; width: 557px; height: 162px; background: var(--stage-deep); }
  .related h4 { position: absolute; left: 39px; top: 7px; font-size: 11px; color: #2b4a5e; }
  .thumb { position: absolute; top: 41px; width: 64px; text-align: center; }
  .thumb .shot { width: 64px; height: 64px; background: linear-gradient(135deg, #ffffff 0%, #cfd2d5 100%); }
  .thumb a { display: block; margin-top: 5px; font-size: 10px; color: var(--thumb-link); text-decoration: underline; white-space: nowrap; }

  /* Footer */
  .footer { position: absolute; left: 37px; top: 1039px; width: 864px; height: 108px; background: linear-gradient(180deg, var(--footer-top) 0%, var(--stage-deep) 55%); }
  .footer-brand { position: absolute; left: 68px; top: 40px; font-family: "Open Sans", sans-serif; font-weight: 700; font-size: 15px; color: #ffffff; }
  .footer-col { position: absolute; top: 25px; font-size: 6.5px; line-height: 9px; }
  .footer-col b { display: block; color: #ffffff; }
  .footer-col p { color: var(--link-light); margin-bottom: 7px; }
  .footer-col .on { color: #ffffff; font-weight: 700; }
</style>
</head>
<body>
<div class="canvas">
  <div class="stage"></div>

  <header>
    <div class="brand"><span class="brand-mark"></span><span class="brand-name">Lorvika</span></div>
    <div class="brand-tagline">Entreprenerielle metoder i undervisningen</div>
    <nav class="breadcrumb">Hjem &gt; Good examples &gt; <span class="current">Smått-VERK at Brekkelia school</span></nav>
  </header>

  <aside class="side-panel">
    <ul class="main-nav">
      <li>What is pedagogical<br>entrepreneurship</li>
      <li>Methods and<br>teaching plans</li>
      <li class="active">Good examples/<br>best pratice</li>
    </ul>
    <div class="multimedia">
      <h3>Multimedia</h3>
      <div class="media-tabs"><span>video (1)</span><span>images (5)</span></div>
      <div class="video-frame" role="img" aria-label="Video from the classroom project">
        <svg width="165" height="10" viewBox="0 0 165 10">
          <polygon points="0,0 9,5 0,10" fill="#1c4f70"/>
          <rect x="13" y="3" width="120" height="4" fill="none" stroke="#1c4f70" stroke-width="1"/>
          <g fill="#1c4f70"><rect x="138" y="2" width="1.5" height="6"/><rect x="141" y="2" width="1.5" height="6"/><rect x="144" y="2" width="1.5" height="6"/><rect x="147" y="2" width="1.5" height="6"/></g>
        </svg>
      </div>
    </div>
  </aside>

  <main class="main-panel">
    <nav class="utility-nav">
      <a>best pratice school</a><a>Try lorvikameter</a><a>about lorvika.no</a>
    </nav>
    <form class="search">
      <input type="text" value="search ...">
      <button type="button" aria-label="Search">
        <svg width="10" height="10" viewBox="0 0 10 10"><circle cx="4" cy="4" r="3" fill="none" stroke="#fff" stroke-width="1.3"/><line x1="6.2" y1="6.2" x2="9.5" y2="9.5" stroke="#fff" stroke-width="1.3"/></svg>
      </button>
    </form>

    <section class="article-head">
      <h1>Smått-VERK i Brekkelia</h1>
      <p class="lead">Lorem Ipsum is simply dummy text of the printing and typesetting industry.</p>
      <p class="intro">Lorem Ipsum has been the industry's standard dummy text ever since the 1500s, when an unknown printer took a galley of type and scrambled it to make a type specimen book. It has survived not only five centuries, but also the leap into electronic typesetting, remaining essentially unchanged.</p>
    </section>

    <div class="facts">
      <div class="fact">
        <svg width="24" height="24" viewBox="0 0 24 24"><circle cx="12" cy="12" r="11" fill="#1c5576" stroke="#9aa" stroke-width="1.5"/><circle cx="12" cy="12" r="8" fill="#2e6c8e"/><path d="M12 6v6l4 3" stroke="#fff" stroke-width="1.5" fill="none"/></svg>
        Time spent<br>Text
      </div>
      <div class="fact">
        <svg width="44" height="22" viewBox="0 0 44 22"><polygon points="2,12 24,4 42,10 20,19" fill="#8c8c8c"/><polygon points="4,11 24,5 39,10 20,16" fill="#d0d0d0"/></svg>
        Subject<br>English, Norwegian
      </div>
      <div class="fact">
        <svg width="36" height="22" viewBox="0 0 36 22"><rect x="4" y="4" width="28" height="16" rx="2" fill="#8a8a8a"/><rect x="7" y="7" width="10" height="10" fill="#b4b4b4"/></svg>
        Method<br>VERK
      </div>
    </div>

    <div class="school-card">
      <div class="school-id"><span class="badge"></span><div><b>Brekkelia skole</b><small>4th grade</small></div></div>
      <div class="school-photo" role="img" aria-label="Photo of the school"></div>
      <div class="contact">
        <svg width="12" height="30" viewBox="0 0 12 30"><circle cx="6" cy="6" r="5.5" fill="#9a9a9a"/><rect x="1" y="14" width="10" height="16" rx="2" fill="#b3b3b3"/></svg>
        <div><b>Contact</b><small>John Doe</small></div>
      </div>
    </div>

    <article class="article-body">
      <h2>This is how we did it</h2>
      <p>Lorem Ipsum is simply dummy text of the printing and typesetting industry. Lorem Ipsum has been the industry's standard dummy text ever since the 1500s, when an unknown printer took a galley of type and scrambled it to make a type specimen book. It has survived not only five centuries, but also the leap into electronic typesetting, remaining essentially unchanged.</p>
      <h3>Title</h3>
      <p>Lorem Ipsum is simply dummy text of the printing and typesetting industry. Lorem Ipsum has been the industry's standard dummy text ever since the 1500s, when an unknown printer took a galley of type and scrambled it to make a type specimen book.</p>
      <p>It has survived not only five centuries, but also the leap into electronic typesetting, remaining essentially unchanged.</p>
      <h3>Title</h3>
      <p>Lorem Ipsum is simply dummy text of the printing and typesetting industry. Lorem Ipsum has been the industry's standard dummy text ever since the 1500s, when an unknown printer took a galley of type and scrambled it to make a type specimen book. It has survived not only five centuries, but also the leap into electronic typesetting, remaining essentially unchanged.</p>
    </article>

    <section class="related">
      <h4>You might wanto to see</h4>
      <div class="thumb" style="left:39px"><div class="shot" role="img" aria-label="Related example image"></div><a>Lorem ipsum</a></div>
      <div class="thumb" style="left:164px"><div class="shot" role="img" aria-label="Related example image"></div><a>Lorem ipsum</a></div>
      <div class="thumb" style="left:303px"><div class="shot" role="img" aria-label="Related example image"></div><a>Lorem ipsum</a></div>
      <div class="thumb" style="left:442px"><div class="shot" role="img" aria-label="Related example image"></div><a>Lorem ipsum</a></div>
    </section>
  </main>

  <footer class="footer">
    <div class="footer-brand">Lorvika</div>
    <div class="footer-col" style="left:165px">
      <b>Pedagogical entrepreneurship</b>
      <p>What is pedagogical entrepreneurship? | Science | Best pratice schools | Lorvikameter | About lorvika.no</p>
      <b>Gode eksempler</b>
      <p>Smått-VERK at Brekkelia school | Smått-VERK at Brekkelia school | Smått-VERK at Brekkelia | more...</p>
    </div>
    <div class="footer-col" style="left:559px">
      <b>Teaching Plans</b>
      <p>Lorem ipsum | Lorem ipsum | Lorem ipsum | Lorem ipsum | more...</p>
      <b>Methods</b>
      <p>Story line | <span class="on">VERK</span> | Café-pedagogikk | more...</p>
    </div>
  </footer>
</div>
</body>
</html>
```